Audio Visual & Broadcast Installing Company needs a Web Site Design

We need a website design for our company Halvern Crane Ltd. We are a small company that does Audio Visual and broadcast installations. We are looking to expand our business and need a professional web presence. All work completed by us is done to a very high standard and it’s this attention to detail that sets us apart from our competitors. Our projects include doing fibre optics at major sporting events; installing and commissioning bespoke control systems on super yachts and installing the latest systems in luxury homes.

We provide the following services:
System design
On-site installation
Rack building
Pre-fabricated cable looms
Fibre optic cabling

We would like a website that gives details of our services and provides contact information. Our customers are other businesses and our website needs to reflect this. The flyer attached will be used to promote the company and we would like the website to follow this theme. Please use the colours from our logo, as the colour scheme. We know that our colours are bright and we don’t want them to overwhelm the site. With our website we want to communicate that we are professional and provide a quality service.
NB UPDATE: please use stock images for any graphical elements.

The following 3 sites belong to some of our competitors. The first 2, we DON'T like because they don't project a professional feeling. The last one, 'lumatrexlinks', is better as it provides the required information in a clear, simple form.

http://www.qorvamedia.example/

http://www.pellisforthwiring.example/

http://www.lumatrexlinks.example/

We really like the following site, it feels professional and high end without too many flashy graphics. We want something that is fast to load but still shows the high end quality of our work.

http://oberlyncraft.example/

Pages/Sections

Home
On site installation
Rack building and cable looms
Fibre optics
Portfolio (this will be limited to start with but must be easy to expand and add new projects)
Updates

Target Market(s)

Businesses operating in the following areas:
Audio Vision, Broadcasting, Home Automation, Events

Industry/Entity Type

Broadcasting

Coding

Coded - Design and coding required

Number of Pages Required

4 page

Font styles to use
Other font styles liked:
• similar to attached flyer

Requirements
Must have
• The same theme as the 'flyer1' attachment.

```html
<!DOCTYPE html>
<html lang="en">
<head>
<meta charset="utf-8">
<title>Halvern Crane Ltd – Broadcast &amp; AV Cabling</title>
<link rel="stylesheet" href="https://fonts.googleapis.com/css2?family=Open+Sans:ital,wght@0,400;0,600;0,700;1,400&family=Raleway:wght@300;400&display=swap">
<style>
:root{
  --orange-light:#fb7d22;
  --orange-mid:#f6612f;
  --orange-red:#ef4b3c;
  --btn-top:#ff9a1e;
  --btn-bottom:#f23a1e;
  --btn-edge:#b5102a;
  --night:#1c2130;
  --night-soft:#3a4158;
  --edge-blue:#1f6fd6;
  --white:#ffffff;
  --ink:#111111;
  --accent-pink:#d6164f;
  --muted:#8a8a8a;
}
*{box-sizing:border-box;margin:0;padding:0}
html,body{width:1200px;height:833px;overflow:hidden}
body{font-family:"Open Sans",Arial,sans-serif;color:var(--white)}
.page{
  position:relative;width:1200px;height:833px;overflow:hidden;
  background:linear-gradient(100deg,var(--orange-red) 0%,var(--orange-mid) 30%,var(--orange-light) 60%,var(--orange-mid) 100%);
}
.backdrop{position:absolute;left:0;top:0}
.brand{position:absolute;left:78px;top:58px;display:flex;align-items:center;gap:12px}
.brand-mark{width:28px;height:28px;background:var(--white);opacity:.85;border-radius:4px}
.brand-name{font-size:30px;font-weight:600;color:var(--white);letter-spacing:-.5px}
.main-nav a{position:absolute;left:90px;font-size:17px;color:var(--white);text-decoration:none}
.main-nav a.is-active{
  left:77px;top:146px;width:172px;height:42px;padding:9px 0 0 13px;color:var(--ink);
  background:linear-gradient(180deg,var(--btn-top),var(--btn-bottom));
  border-bottom:3px solid var(--btn-edge);border-right:3px solid var(--btn-edge);
  box-shadow:0 2px 4px rgba(0,0,0,.35);
}
.video{
  position:absolute;left:76px;top:454px;width:482px;height:241px;border:2px solid #e8e8e8;
  background:linear-gradient(135deg,#6a6a6a 0%,#3b3b3b 40%,#1b1b1b 70%,#4a3a2a 100%);
}
.video-play{position:absolute;left:184px;top:94px;width:100px;height:74px;border:2px solid var(--white)}
.video-play::after{content:"";position:absolute;left:38px;top:20px;border-left:28px solid var(--white);border-top:15px solid transparent;border-bottom:15px solid transparent}
.section-title{position:absolute;font-family:"Raleway",sans-serif;font-weight:300;font-size:32px;text-align:center;width:560px;left:570px}
.title-rule{position:absolute;left:782px;width:137px;height:1px;background:var(--white)}
.services-intro{position:absolute;left:585px;top:117px;width:530px;font-size:14px;line-height:21px;text-align:center}
.service{position:absolute;top:226px;width:110px;text-align:center;font-size:14px;font-weight:600;line-height:19px}
.service svg{display:block;margin:0 auto 6px;width:36px;height:36px}
.divider{position:absolute;left:335px;top:372px;width:865px;border-top:1px dashed rgba(255,255,255,.8)}
.tagline{position:absolute;left:570px;top:496px;width:560px;text-align:center;font-size:16px;font-weight:700}
.welcome-text{position:absolute;left:600px;top:530px;width:500px;font-size:14.5px;line-height:21px;text-align:center}
.btn{position:absolute;top:633px;height:52px;font-size:18px;text-align:center;line-height:50px;text-decoration:none;box-shadow:0 2px 4px rgba(0,0,0,.4)}
.btn-light{left:643px;width:177px;background:var(--white);color:var(--accent-pink);border-right:3px solid #cfcfcf;border-bottom:3px solid #cfcfcf}
.btn-warm,.subscribe{background:linear-gradient(180deg,var(--btn-top),var(--btn-bottom));color:var(--ink);border-right:3px solid var(--btn-edge);border-bottom:3px solid var(--btn-edge)}
.btn-warm{left:834px;width:182px}
.contact-title{position:absolute;left:80px;top:720px;font-family:"Raleway",sans-serif;font-size:20px}
.contact-line{position:absolute;display:flex;align-items:center;gap:12px;font-size:14px}
.contact-line svg{width:22px;height:20px;fill:var(--white)}
.contact-phone{font-size:16px}
.email-field{position:absolute;left:697px;top:771px;width:292px;height:36px;background:var(--white);border:none;padding-left:12px;font-style:italic;font-size:12px;color:var(--muted);line-height:36px}
.subscribe{position:absolute;left:993px;top:766px;width:128px;height:50px;font-size:18px;text-align:center;line-height:48px;box-shadow:0 2px 4px rgba(0,0,0,.35)}
</style>
</head>
<body>
<div class="page">
  <svg class="backdrop" width="1200" height="833" viewBox="0 0 1200 833">
    <defs>
      <radialGradient id="nightGlow" cx="0.45" cy="0.55" r="0.8">
        <stop offset="0" stop-color="var(--night-soft)"/>
        <stop offset="0.6" stop-color="#262c3d"/>
        <stop offset="1" stop-color="#0c0f16"/>
      </radialGradient>
    </defs>
    <path d="M612 0 C548 190 420 360 140 515 L140 610 C400 748 800 748 1200 676 L1200 0 Z" fill="var(--edge-blue)"/>
    <path d="M625 0 C560 200 425 365 150 520 L150 600 C400 735 800 735 1200 665 L1200 0 Z" fill="url(#nightGlow)"/>
  </svg>

  <div class="brand"><span class="brand-mark"></span><span class="brand-name">Halvern Crane</span></div>

  <nav class="main-nav">
    <a class="is-active" href="#">Home</a>
    <a href="#" style="top:203px">On site installation</a>
    <a href="#" style="top:249px">Rack building and cable</a>
    <a href="#" style="top:295px">looms</a>
    <a href="#" style="top:341px">Fiber Optics</a>
    <a href="#" style="top:387px">Portfolio</a>
  </nav>

  <div class="video" role="img" aria-label="Video still of hands connecting fibre optic cables in an equipment rack"><span class="video-play"></span></div>

  <h2 class="section-title" style="top:36px">Our Services</h2>
  <span class="title-rule" style="top:92px"></span>
  <p class="services-intro">Halvern Crane provide cablong services for Broadcast Television and Audion VisualSystem.With over 15 years experience working in these industries we can help with every aspect of design, project management, installation and maintenance.</p>

  <div class="service" style="left:587px">
    <svg viewBox="0 0 36 36" fill="var(--white)"><path d="M8 10 L26 28 A13 13 0 0 1 8 10Z"/><rect x="12" y="28" width="12" height="4"/><circle cx="24" cy="12" r="2.5"/></svg>
    Broadcast/<br>AV System<br>Design</div>
  <div class="service" style="left:694px">
    <svg viewBox="0 0 36 36" fill="var(--white)"><rect x="4" y="16" width="28" height="10" rx="3"/><circle cx="11" cy="28" r="3"/><circle cx="25" cy="28" r="3"/><circle cx="18" cy="9" r="5"/></svg>
    On-site<br>Installation</div>
  <div class="service" style="left:801px">
    <svg viewBox="0 0 36 36" fill="none" stroke="var(--white)" stroke-width="3"><path d="M7 3V33M29 3V33M18 3V33M7 10H29M7 18H29M7 26H29"/></svg>
    Rack Building</div>
  <div class="service" style="left:908px">
    <svg viewBox="0 0 36 36" fill="none" stroke="var(--white)" stroke-width="2"><path d="M11 14 V30 Q18 35 25 30 V14 Q18 10 11 14Z"/><path d="M14 4V14M18 3V13M22 4V14"/></svg>
    Pre-<br>fabricated<br>Cable Looms</div>
  <div class="service" style="left:1016px">
    <svg viewBox="0 0 36 36" fill="none" stroke="var(--white)" stroke-width="2"><circle cx="18" cy="10" r="3"/><path d="M12 4A9 9 0 0 0 12 16M24 4A9 9 0 0 1 24 16M18 13V30M8 31H28"/></svg>
    Fiber optic<br>installation</div>

  <span class="divider"></span>

  <h1 class="section-title" style="top:412px">Welcome to The Halvern Crane</h1>
  <span class="title-rule" style="top:468px"></span>
  <p class="tagline">Making the connections that digital innovation demands.</p>
  <p class="welcome-text">Our projects range from fiber optic cabling at major sport events to installing and commisioning bespoke control system on some of the worlds largest super yachts. The company based in London has executed projects sucessfully across Europe.</p>
  <a class="btn btn-light" href="#">Read More</a>
  <a class="btn btn-warm" href="#">View Our Projects</a>

  <h3 class="contact-title">Contact Us</h3>
  <p class="contact-line" style="left:78px;top:762px">
    <svg viewBox="0 0 22 20"><path d="M11 1 L21 10 H18 V19 H13 V13 H9 V19 H4 V10 H1Z"/></svg>123 Street, Landmark, Counter 123456</p>
  <p class="contact-line contact-phone" style="left:78px;top:792px">
    <svg viewBox="0 0 22 20"><path d="M5 1 L9 5 L7 8 Q9 12 13 14 L16 12 L20 16 L17 19 Q4 17 2 4Z"/></svg>01234 123-4567</p>
  <p class="contact-line" style="left:258px;top:792px">
    <svg viewBox="0 0 26 20" style="width:28px"><path d="M1 2H25V18H1Z M3 4 L13 12 L23 4" fill="none" stroke="var(--white)" stroke-width="2"/></svg>info@halverncrane.example</p>

  <div class="email-field">Enter Email</div>
  <div class="subscribe">Subscribe</div>
</div>
</body>
</html>
```